Business card for Mortgage broker business

I have already had the logo designed and am needing a great looking business card. My business focus is on servicing clients who may not be able to obtain finance through traditional lenders due to bad credit, short term employment or they just don't fit the banks profile. It needs to be professional, trust worthy but also have a caring fell about it.
I have provided files showing the green and black logo, the white logo(on white background so the file looks blank) and also a file with the white logo with a background of leaves that was made up which will probably be used for a website header.

Industry/Entity Type

Finance

Contact Information for Business Card

Marcus Dalby
Managing Director, Accredited Finance Broker(AFB)
Po Box 817, Glenmere VIC 3921
marcus@kestrelfunding.com.au
www.kestrelfunding.com.au
0438 216 507

Requirements
Nice to have
• I have added a picture of myself as I would like to see some designs with the pic in it, but I'm not sure if I want it on there with the logo's or just the logo's

```html
<!DOCTYPE html>
<html lang="en">
<head>
<meta charset="utf-8">
<title>Kestrel Funding – Business Card</title>
<link rel="stylesheet" href="https://fonts.googleapis.com/css2?family=Noticia+Text:wght@400&display=swap">
<style>
  :root {
    --page-bg: #ececec;
    --card-white: #f5f5f5;
    --brand-green: #1d6b40;
    --brand-green-deep: #14603a;
    --text-dark: #3c3c3c;
    --text-muted: #6a6a6a;
    --photo-light: #b9b3ad;
    --photo-dark: #2d2a2a;
  }
  * { margin: 0; padding: 0; box-sizing: border-box; }
  html, body {
    width: 1200px;
    height: 1000px;
    overflow: hidden;
    background: var(--page-bg);
    font-family: "Noticia Text", Georgia, serif;
  }
  .canvas {
    position: relative;
    width: 1200px;
    height: 1000px;
  }
  .card {
    position: absolute;
    width: 520px;
    height: 298px;
    box-shadow: 0 14px 30px rgba(0, 0, 0, 0.18);
  }

  /* Front */
  .card-front {
    left: 70px;
    top: 170px;
    background: linear-gradient(135deg, #ffffff 0%, #ffffff 12%, #a9c9b5 45%, #5f9b77 70%, var(--brand-green-deep) 100%);
    display: flex;
    align-items: center;
    justify-content: center;
  }
  .front-brand {
    color: #ffffff;
    font-size: 40px;
    font-weight: 400;
    letter-spacing: 3px;
    text-align: center;
    line-height: 1.1;
  }

  /* Back */
  .card-back {
    left: 610px;
    top: 500px;
    background: var(--card-white);
  }
  .back-brand {
    position: absolute;
    left: 28px;
    top: 130px;
    width: 170px;
    color: var(--brand-green);
    font-size: 22px;
    font-weight: 400;
    letter-spacing: 1px;
    line-height: 1.15;
    text-align: center;
  }
  .divider {
    position: absolute;
    left: 214px;
    top: 46px;
    width: 2px;
    height: 210px;
    background: var(--brand-green);
  }
  .portrait-frame {
    position: absolute;
    left: 240px;
    top: 34px;
    width: 116px;
    height: 116px;
    border: 1px solid var(--brand-green);
    padding: 5px;
    background: #ffffff;
  }
  .portrait {
    display: block;
    width: 100%;
    height: 100%;
  }
  .contact {
    position: absolute;
    left: 240px;
    top: 158px;
    line-height: 1.3;
  }
  .contact-name {
    color: var(--brand-green);
    font-size: 19px;
  }
  .contact-title {
    color: var(--text-muted);
    font-size: 8.5px;
    margin-bottom: 4px;
  }
  .contact-address {
    color: var(--text-dark);
    font-size: 12.5px;
  }
  .contact-link {
    color: var(--brand-green);
    font-size: 12.5px;
  }
</style>
</head>
<body>
<main class="canvas">
  <section class="card card-front" aria-label="Business card front">
    <div class="front-brand">Kestrel Funding</div>
  </section>

  <section class="card card-back" aria-label="Business card back">
    <div class="back-brand">Kestrel Funding</div>
    <div class="divider"></div>
    <div class="portrait-frame">
      <svg class="portrait" viewBox="0 0 100 100" role="img" aria-label="Portrait photo of Marcus Dalby">
        <defs>
          <linearGradient id="portraitTone" x1="0" y1="0" x2="0" y2="1">
            <stop offset="0" stop-color="#f2f2f2"/>
            <stop offset="0.55" stop-color="#b9b3ad"/>
            <stop offset="1" stop-color="#2d2a2a"/>
          </linearGradient>
        </defs>
        <rect width="100" height="100" fill="url(#portraitTone)"/>
      </svg>
    </div>
    <div class="contact">
      <div class="contact-name">Marcus Dalby</div>
      <div class="contact-title">Managing Director, Accredited Finance Broker (AFB)</div>
      <div class="contact-address">Po Box 817, Glenmere VIC 3921</div>
      <div class="contact-link">marcus@kestrelfunding.com.au</div>
      <div class="contact-link">www.kestrelfunding.com.au</div>
      <div class="contact-link">0438 216 507</div>
    </div>
  </section>
</main>
</body>
</html>
```